Mortgage Broker Site

Need a custom design for a mortgage broker site - please refer to the attached Word .doc that gives more detail.

Number of Pages Required

5+ page

Colors

Designer to choose colors to be used in the design.

```html
<!DOCTYPE html>
<html lang="en">
<head>
<meta charset="utf-8">
<title>Arbora Mortgage</title>
<link href="https://fonts.googleapis.com/css2?family=Poppins:wght@500;600;700&family=Roboto:wght@400;500;700&display=swap" rel="stylesheet">
<style>
:root{
  --red:#8e0618;
  --ink:#111;
  --muted:#666;
  --line:#ddd;
  --soft:#f7f7f7;
  --white:#fff;
}
*{margin:0;padding:0;box-sizing:border-box}
html,body{width:753px;height:1200px;overflow:hidden;background:var(--white);font-family:Roboto,Arial,sans-serif;color:var(--ink)}
.page{position:relative;width:753px;height:1200px}
.abs{position:absolute}
.hero-art{position:absolute;left:0;top:0}
.brand{font-family:Poppins,sans-serif;font-weight:600;color:var(--white);font-size:16px;left:39px;top:9px}
.nav a{position:absolute;top:15px;font-size:7px;color:#eee;text-decoration:none}
.btn{position:absolute;display:flex;align-items:center;justify-content:center;font-size:6px;font-weight:700;letter-spacing:.3px;color:var(--white);text-transform:uppercase}
.btn-red{background:var(--red)}
.btn-ghost{border:1px solid var(--white)}
.hero-title{left:146px;top:116px;font-family:Poppins,sans-serif;font-weight:700;font-size:25px;color:var(--white)}
.hero-text{left:147px;top:161px;width:230px;font-size:7.8px;line-height:11.8px;color:#f2f2f2}
.center{left:0;width:753px;text-align:center}
.h2{font-family:Poppins,sans-serif;font-weight:600;color:var(--ink)}
.sub{font-size:6.5px;color:var(--muted)}
.card{position:absolute;top:477px;width:188px;height:141px;border:1px solid var(--line);background:var(--white);text-align:center}
.card-left{left:183px;border-top:4px solid var(--red);border-left:4px solid var(--red)}
.card-right{left:383px;border-top:4px solid var(--red);border-right:4px solid var(--red)}
.card svg{margin-top:26px}
.card h3{font-family:Poppins,sans-serif;font-weight:500;font-size:10px;margin-top:9px}
.card p{font-size:6.3px;line-height:9.5px;color:var(--muted);margin-top:5px;padding:0 26px}
.search{left:226px;top:750px;width:236px;height:23px;border:1px solid #ccc;background:var(--white)}
.band{left:0;width:753px;background:var(--soft)}
.houses{left:0;top:940px;width:753px;height:44px;background:linear-gradient(#f7f7f7,#ececec)}
.col{position:absolute;top:1017px}
.col h4{font-family:Poppins,sans-serif;font-weight:500;font-size:10px;margin-bottom:12px}
.col a{display:block;font-size:6.3px;color:#444;text-decoration:none;line-height:8px;margin-bottom:6px}
.dot{display:inline-block;width:14px;height:14px;border-radius:50%;margin-right:2px}
.legal{left:214px;font-size:4.4px;color:#333}
</style>
</head>
<body>
<div class="page">

  <svg class="hero-art" width="753" height="378" viewBox="0 0 753 378" role="img" aria-label="Hero photo of a smiling couple holding house keys and a small model home">
    <defs>
      <linearGradient id="heroTone" x1="0" y1="0" x2="1" y2="0">
        <stop offset="0" stop-color="#6d6468"/>
        <stop offset=".55" stop-color="#5d5659"/>
        <stop offset=".8" stop-color="#8f7a78"/>
        <stop offset="1" stop-color="#b9a3a1"/>
      </linearGradient>
    </defs>
    <polygon points="0,0 753,0 753,313 376,373 0,313" fill="url(#heroTone)"/>
    <polyline points="0,315 376,375 753,315" fill="none" stroke="#8e0618" stroke-width="4"/>
    <rect x="372" y="330" width="9" height="15" rx="4.5" fill="none" stroke="#fff" stroke-width="1"/>
    <line x1="376.5" y1="334" x2="376.5" y2="349" stroke="#fff" stroke-width=".8"/>
  </svg>

  <div class="abs brand">Arbora</div>
  <nav class="nav">
    <a style="left:115px">Rates</a>
    <a style="left:145px">Purchase</a>
    <a style="left:187px">Refinance</a>
    <a style="left:546px">&#9742; Schedule a Call</a>
    <a style="left:608px">&#9636; Guides</a>
  </nav>
  <div class="btn btn-red" style="left:651px;top:8px;width:63px;height:22px">Apply Now</div>

  <h1 class="abs hero-title">Arbora Mortgage</h1>
  <p class="abs hero-text">Lorem ipsum dolor sit amet, consectetur adipiscing elit, sed do eiusmod tempor incididunt ut labore et dolore magna aliqua ut enim ad minim veniam.</p>
  <div class="btn btn-red" style="left:147px;top:217px;width:95px;height:22px">Purchase Rates</div>
  <div class="btn btn-ghost" style="left:254px;top:217px;width:94px;height:22px">Refinance Rates</div>

  <h2 class="abs center h2" style="top:416px;font-size:15px">Mortgage Tools</h2>
  <p class="abs center sub" style="top:439px">Lorem ipsum dolor sit amet, consectetur adipiscing elit</p>

  <div class="card card-left">
    <svg width="24" height="29" viewBox="0 0 24 29" fill="none" stroke="#8e0618" stroke-width="1">
      <rect x=".5" y="2.5" width="23" height="26"/>
      <path d="M9 6l3-3 3 3v2H9z"/>
      <rect x="3" y="10" width="8" height="7"/><rect x="13" y="10" width="8" height="7"/>
      <rect x="3" y="19" width="8" height="7"/><rect x="13" y="19" width="8" height="7"/>
      <path d="M7 11.5v4M5 13.5h4M15 13.5h4M5 20.5l4 4M9 20.5l-4 4M15 21.5h4M15 23.5h4"/>
    </svg>
    <h3>Mortgage Calculator</h3>
    <p>See how much you can afford by home price, monthly payment, or income.</p>
  </div>
  <div class="card card-right">
    <svg width="24" height="29" viewBox="0 0 24 29" fill="none" stroke="#8e0618" stroke-width="1">
      <path d="M.5.5h15v28H.5z"/>
      <path d="M3 4h9M3 7h9M3 10h6"/>
      <circle cx="19" cy="11" r="4.5"/><path d="M19 8.5v5M17.5 10h3M17.5 12h3"/>
      <path d="M4 24l8-10 2 2-8 10z"/>
      <path d="M12 28v-6l5-4 6 4v6zM16 28v-3h3v3"/>
    </svg>
    <h3>Home Value Checker</h3>
    <p>Should you refinance? This calculator breaks down monthly and lifetime cost.</p>
  </div>

  <h2 class="abs center h2" style="top:664px;font-size:14.5px;line-height:17px">2020 Mortgage Loan Limits For Conventional,<br>FHA, &amp; VA Loans</h2>
  <p class="abs center" style="top:705px;font-size:7.8px;line-height:12px;color:var(--muted)">Mortgage loan limits for every U.S. county, as published by Keystone Home Finance &amp; Northgate Mortgage Corp, the Federal Housing<br>Administration (FHA), and the Department of Veterans Affairs (VA)</p>
  <div class="abs search"></div>
  <div class="btn btn-red" style="left:465px;top:750px;width:62px;height:23px">Search</div>

  <div class="abs band" style="top:820px;height:165px"></div>
  <h2 class="abs center h2" style="top:861px;font-size:13px">Connect with America’s Lending Experts Today!</h2>
  <div class="abs center" style="top:882px;font-family:Poppins,sans-serif;font-weight:600;font-size:21px;color:var(--red)">(555) 210-4870</div>
  <div class="abs houses" role="img" aria-label="Faint line pattern of a row of houses"></div>

  <div class="col" style="left:146px"><h4>Links</h4><a>Get a Mortgage Rate Now</a><a>Load Types</a><a>Arbora Disclosures</a><a>Confarming, VA &amp; FHA<br>Loan Limits</a></div>
  <div class="col" style="left:265px"><h4>Company</h4><a>About Us</a><a>Careers</a><a>Arbora Resources</a><a>Contact</a></div>
  <div class="col" style="left:382px"><h4>Policies</h4><a>Security Policy</a><a>Privacy Policy</a><a>Terms of Use</a><a>Email Policy</a></div>
  <div class="col" style="left:500px"><h4>Social Media</h4>
    <span class="dot" style="background:#1565c0"></span><span class="dot" style="background:#1ea1f2"></span><span class="dot" style="background:#d0021b"></span><span class="dot" style="background:#f26522"></span>
  </div>

  <div class="abs band" style="top:1126px;height:74px"></div>
  <div class="btn btn-red" style="left:582px;top:1115px;width:24px;height:24px;border-radius:50%;font-size:3.6px;line-height:4px;text-align:center">Scroll<br>to top</div>
  <div class="abs" style="left:147px;top:1150px;font-family:Poppins,sans-serif;font-weight:600;font-size:16px;color:var(--red)">Arbora</div>
  <p class="abs legal" style="top:1150px;color:#111">Arbora NMLS #418260. Click here to view our licensing with the NMLS and DRE</p>
  <p class="abs legal" style="top:1160px">2009-2020 Copyright Arbora, Inc. All rights reserved.</p>
  <p class="abs legal" style="top:1167px">Lending services provided by Arbora, Inc dba Arbora. Rates, program terms and conditions are subject to change without notice.</p>
</div>
</body>
</html>
```